Rivex Management LLC Business Card

The sample logo was attached for the business Card Design for Traffic Control Company named Rivex Management LLC. Card design needs to have the company logo and colors match the logo color. It will be nice to show some images of Traffic control signs or cones, even roads closer that math the company services

Target Market(s)

Temporary traffic control. Road closer.

Industry/Entity Type

Construction

Contact Information for Business Card

basic information, name, job title, address, email phone, website

Font styles to use
Serif
Sans Serif

Colors
F0912C
F2A743
F7CA91
FBE8D2
FDF5EE
EE7325
F08F49
F5BC92
FAE3D3
FDF4ED

```html
<!DOCTYPE html>
<html lang="en">
<head>
<meta charset="utf-8">
<title>Rivex Management LLC Business Card</title>
<link rel="stylesheet" href="https://fonts.googleapis.com/css2?family=Montserrat:wght@400;500;700;800&display=swap">
<style>
  :root {
    --orange: #EE7325;
    --orange-soft: #F08F49;
    --cone-light: #F5BC92;
    --charcoal: #4a4a4c;
    --ink: #1d1d1d;
    --card: #ffffff;
    --backdrop: #2e2e30;
  }
  * { box-sizing: border-box; margin: 0; padding: 0; }
  html, body {
    width: 1200px; height: 960px; overflow: hidden;
    background: var(--backdrop);
    font-family: "Montserrat", Arial, sans-serif;
  }
  .canvas { position: relative; width: 1200px; height: 960px; }
  .card {
    position: absolute;
    width: 620px; height: 354px;
    background: var(--card);
    box-shadow: 0 10px 24px rgba(0,0,0,.45);
  }
  .card--front { left: 70px; top: 60px; }
  .card--back { left: 510px; top: 530px; }

  /* front */
  .front__artwork {
    position: absolute; left: 150px; top: 34px;
    width: 320px; height: 110px;
    background: linear-gradient(90deg, var(--orange) 0%, var(--cone-light) 50%, var(--orange-soft) 100%);
    border-radius: 4px;
  }
  .brand {
    color: var(--orange);
    font-weight: 800;
    letter-spacing: .02em;
    line-height: 1.1;
  }
  .front__brand {
    position: absolute; left: 0; right: 0; top: 182px;
    text-align: center; font-size: 44px;
  }
  .front__brand .brand-sub { display: block; font-size: 44px; }

  /* back */
  .back__brand {
    position: absolute; left: 36px; top: 112px; width: 262px;
    font-size: 27px; display: flex; align-items: center; gap: 12px;
  }
  .brand-mark {
    flex: none; width: 16px; height: 16px; border-radius: 50%;
    background: var(--orange);
  }
  .back__divider {
    position: absolute; left: 318px; top: 50px;
    width: 2px; height: 190px; background: var(--orange);
  }
  .contact {
    position: absolute; left: 340px; top: 48px; right: 20px;
    color: var(--ink); font-size: 14px; font-weight: 500; line-height: 1.4;
    white-space: nowrap;
  }
  .contact__name {
    color: var(--orange); font-weight: 800; font-size: 20px;
    letter-spacing: .02em; text-transform: uppercase;
  }
  .contact__role { margin-bottom: 8px; }
  .contact__address { margin-bottom: 10px; }
  .contact__list { list-style: none; }
  .contact__list li { display: flex; align-items: center; gap: 10px; margin-bottom: 3px; }
  .contact__list svg { width: 14px; height: 14px; flex: none; }
  .tagline {
    position: absolute; left: 0; right: 0; bottom: 34px;
    text-align: center; color: var(--ink); font-size: 15px; font-weight: 500;
  }
</style>
</head>
<body>
<main class="canvas">

  <section class="card card--front">
    <div class="front__artwork" role="img" aria-label="Illustration of traffic cones and road signs"></div>
    <h1 class="brand front__brand">Rivex<span class="brand-sub">Management LLC</span></h1>
  </section>

  <section class="card card--back">
    <div class="brand back__brand"><span class="brand-mark"></span><span>Rivex Management LLC</span></div>
    <div class="back__divider"></div>
    <div class="contact">
      <p class="contact__name">Colin Hartwell</p>
      <p class="contact__role">Owner/Director</p>
      <p class="contact__address">Brightway Plaza 2100 Elm<br>Crestfield Ave Suite 310</p>
      <ul class="contact__list">
        <li>
          <svg viewBox="0 0 24 24" aria-hidden="true"><path fill="#EE7325" d="M6.6 10.8a15 15 0 0 0 6.6 6.6l2.2-2.2c.3-.3.7-.4 1-.2 1.1.4 2.3.6 3.6.6.6 0 1 .4 1 1V20c0 .6-.4 1-1 1A17 17 0 0 1 3 4c0-.6.4-1 1-1h3.5c.6 0 1 .4 1 1 0 1.3.2 2.5.6 3.6.1.3 0 .7-.2 1z"/></svg>
          <span>555-214-7730</span>
        </li>
        <li>
          <svg viewBox="0 0 24 24" aria-hidden="true"><rect x="2" y="5" width="20" height="14" rx="1" fill="#EE7325"/><path d="M2 6l10 7 10-7" fill="none" stroke="#fff" stroke-width="1.6"/></svg>
          <span>info@rivexmanagement.com</span>
        </li>
        <li>
          <svg viewBox="0 0 24 24" aria-hidden="true"><circle cx="12" cy="12" r="10" fill="#EE7325"/><path d="M2 12h20M12 2c3 3 3 17 0 20M12 2c-3 3-3 17 0 20" fill="none" stroke="#fff" stroke-width="1.3"/></svg>
          <span>www.rivexmanagement.com</span>
        </li>
      </ul>
    </div>
    <p class="tagline">Traffic Control Company named Rivex Management LLC.</p>
  </section>

</main>
</body>
</html>
```